Criminal Defense Law Firm needs Stationary design Theme for a Business Card, Envelope, and Letterhea

Our Law Firm is seeking a general design concept for a business card, letterhead, and Envelope.

Our website is WillowcrestTrialDesk.com

A design for these three items is requested to keep branding in place for the firm. Would like to keep the Firm Colors on the website consistent with our branding on business cards, letterheads, and mailing envelopes #10 size to be exact.

We would like business cards printed front and back with Law firm Colors from website.

Letterhead with law firm colors as well. Design is not limited to just the header, but the footer can be utilized as well for email, website, phone, fax, etc.

Simple #10 envelope consisting of the same design principles set out in the previous two designs.

```html
<!DOCTYPE html>
<html lang="en">
<head>
<meta charset="utf-8">
<title>Willowcrest Trial Law Offices – Stationery</title>
<link rel="stylesheet" href="https://fonts.googleapis.com/css2?family=Libre+Baskerville:wght@400&family=Arimo:wght@700&family=Tinos:wght@400;700&display=swap">
<style>
  :root{
    --backdrop:#c9d6d5;
    --teal:#3fd8b8;
    --paper:#ffffff;
    --ink:#111111;
    --gold:#a8925a;
    --olive:#7d8a2c;
    --serif:"Libre Baskerville", Georgia, serif;
    --sans:"Arimo", Arial, sans-serif;
    --detail:"Tinos", "Times New Roman", serif;
  }
  *{box-sizing:border-box;margin:0;padding:0}
  html,body{width:1200px;height:849px;overflow:hidden;background:var(--backdrop)}
  .canvas{position:relative;width:1200px;height:849px}

  .sheet{position:absolute;background:var(--paper);overflow:hidden}

  /* firm name lockup */
  .brand{position:absolute;display:flex;align-items:center;gap:var(--gap,10px)}
  .brand-dot{flex:none;width:var(--dot,40px);height:var(--dot,40px);border:2px solid var(--ink);border-radius:50%}
  .brand-name{font-family:var(--serif);color:var(--ink);font-size:var(--fs,16px);line-height:1.15;letter-spacing:.03em;text-transform:uppercase}

  /* footer band */
  .footer{position:absolute;left:0;right:0;bottom:0;background:var(--teal);border-top:2px solid var(--gold);display:flex;align-items:center}
  .phone{display:flex;align-items:center;font-family:var(--sans);color:var(--paper);font-weight:700}
  .phone-icon{flex:none;background:var(--ink);border-radius:3px;display:flex;align-items:center;justify-content:center}
  .phone-icon svg{fill:var(--paper)}
  .address{font-family:var(--detail);font-weight:700;color:var(--ink);text-align:center;line-height:1.45}

  /* rotated card back */
  .card-back{position:absolute;left:48px;top:79px;width:367px;height:207px;background:var(--teal);transform:rotate(-21.9deg)}
  .card-back .brand{left:60px;top:126px;--dot:34px;--fs:14px;--gap:8px}

  /* card front */
  .card-front{left:269px;top:251px;width:425px;height:242px}
  .card-front .brand{left:20px;top:20px;--dot:32px;--fs:14px;--gap:8px}
  .card-front .tagline{position:absolute;left:120px;width:240px;top:106px;font-family:var(--detail);color:var(--olive);font-size:11.5px;line-height:1.45;text-align:center}
  .card-front .footer{height:75px;padding:0 20px}
  .card-front .phone{gap:12px;font-size:20px}
  .card-front .phone-icon{width:21px;height:23px}
  .card-front .address{font-size:9px;margin-left:auto;margin-right:8px}

  /* letterhead */
  .letterhead{left:771px;top:24px;width:388px;height:502px}
  .letterhead .brand{left:32px;top:25px;--dot:36px;--fs:15px;--gap:9px}
  .letterhead .footer{height:71px;padding:0 14px 0 16px}
  .letterhead .phone{gap:12px;font-size:19px}
  .letterhead .phone-icon{width:20px;height:22px}
  .letterhead .divider{width:1px;align-self:stretch;margin:6px 14px;background:var(--gold)}
  .letterhead .address{font-size:9px;flex:1}

  /* envelope */
  .envelope{left:57px;top:543px;width:762px;height:294px}
  .envelope .brand{left:40px;top:22px;--dot:62px;--fs:24px;--gap:14px}
  .envelope .footer{height:60px;padding:0 44px 0 50px}
  .envelope .phone{gap:20px;font-size:29px}
  .envelope .phone-icon{width:30px;height:30px}
  .envelope .address{font-size:10.5px;margin-left:auto}
</style>
</head>
<body>
<main class="canvas">

  <section class="card-back" aria-label="Business card back">
    <div class="brand">
      <span class="brand-dot"></span>
      <span class="brand-name">Willowcrest Trial<br>Law Offices</span>
    </div>
  </section>

  <section class="sheet card-front" aria-label="Business card front">
    <div class="brand">
      <span class="brand-dot"></span>
      <span class="brand-name">Willowcrest Trial<br>Law Offices</span>
    </div>
    <p class="tagline">If you have been arrested for any criminal offence, do not hesitate to contact our law offices.</p>
    <footer class="footer">
      <div class="phone">
        <span class="phone-icon"><svg width="13" height="15" viewBox="0 0 24 24"><path d="M6.6 10.8a15.1 15.1 0 0 0 6.6 6.6l2.2-2.2c.3-.3.7-.4 1-.2 1.1.4 2.3.6 3.6.6.6 0 1 .4 1 1V20c0 .6-.4 1-1 1C10.6 21 3 13.4 3 4c0-.6.4-1 1-1h3.5c.6 0 1 .4 1 1 0 1.3.2 2.5.6 3.6.1.3 0 .7-.2 1z"/></svg></span>
        505.555.0148
      </div>
      <p class="address">2140 Alder Street NW<br>Riverton, NM 87110<br>www.willowcresttrialdesk.com</p>
    </footer>
  </section>

  <section class="sheet letterhead" aria-label="Letterhead">
    <div class="brand">
      <span class="brand-dot"></span>
      <span class="brand-name">Willowcrest Trial<br>Law Offices</span>
    </div>
    <footer class="footer">
      <div class="phone">
        <span class="phone-icon"><svg width="12" height="14" viewBox="0 0 24 24"><path d="M6.6 10.8a15.1 15.1 0 0 0 6.6 6.6l2.2-2.2c.3-.3.7-.4 1-.2 1.1.4 2.3.6 3.6.6.6 0 1 .4 1 1V20c0 .6-.4 1-1 1C10.6 21 3 13.4 3 4c0-.6.4-1 1-1h3.5c.6 0 1 .4 1 1 0 1.3.2 2.5.6 3.6.1.3 0 .7-.2 1z"/></svg></span>
        505.555.0148
      </div>
      <span class="divider"></span>
      <p class="address">2140 Alder Street NW<br>Riverton, NM 87110<br>www.willowcresttrialdesk.com</p>
    </footer>
  </section>

  <section class="sheet envelope" aria-label="Number 10 envelope">
    <div class="brand">
      <span class="brand-dot"></span>
      <span class="brand-name">Willowcrest Trial<br>Law Offices</span>
    </div>
    <footer class="footer">
      <div class="phone">
        <span class="phone-icon"><svg width="18" height="20" viewBox="0 0 24 24"><path d="M6.6 10.8a15.1 15.1 0 0 0 6.6 6.6l2.2-2.2c.3-.3.7-.4 1-.2 1.1.4 2.3.6 3.6.6.6 0 1 .4 1 1V20c0 .6-.4 1-1 1C10.6 21 3 13.4 3 4c0-.6.4-1 1-1h3.5c.6 0 1 .4 1 1 0 1.3.2 2.5.6 3.6.1.3 0 .7-.2 1z"/></svg></span>
        505.555.0148
      </div>
      <p class="address">2140 Alder Street NW<br>Riverton, NM 87110<br>www.willowcresttrialdesk.com</p>
    </footer>
  </section>

</main>
</body>
</html>
```